Tarvel Ridge LLC

Need Professional Business cards for New Investment Fund

Target Market(s)

High Quality investors

Industry/Entity Type

Financial

Contact Information for Business Card

Phone Number +1 555 284 6193
Name Pavel Orlinsky
Title Fund Manager
email po@FundTarvel.example
Website www.FundTarvel.example

Colors

Designer to choose colors to be used in the design.

Requirements
Must have
• Must have our Logo and all of the above. Must be made so lettering and loge can be raised

```html
<!DOCTYPE html>
<html lang="en">
<head>
<meta charset="utf-8">
<title>Tarvel Ridge LLC – Business Cards</title>
<link rel="stylesheet" href="https://fonts.googleapis.com/css2?family=Open+Sans:wght@400;600;700&display=swap">
<style>
  :root {
    --backdrop: #ececec;
    --card: #ffffff;
    --green: #6db33f;
    --green-light: #8cc63f;
    --charcoal: #3b3f3a;
    --ink: #4a4a4a;
    --shadow: rgba(0,0,0,0.12);
  }
  * { margin: 0; padding: 0; box-sizing: border-box; }
  html, body {
    width: 1200px; height: 796px; overflow: hidden;
    background: var(--backdrop);
    font-family: "Open Sans", Arial, sans-serif;
  }
  .sheet {
    position: relative; width: 1200px; height: 796px;
    display: flex; align-items: center; justify-content: center; gap: 60px;
  }
  .card {
    position: relative; width: 510px; height: 290px;
    background: var(--card);
    box-shadow: 0 6px 18px var(--shadow);
    overflow: hidden;
  }
  .card__accent {
    position: absolute; right: 0; top: 0; bottom: 0; width: 80px;
    background: linear-gradient(180deg, var(--green-light) 0%, var(--green) 55%, var(--charcoal) 100%);
  }
  .wordmark {
    position: absolute; display: flex; align-items: center; gap: 10px;
    font-weight: 600; color: var(--charcoal); letter-spacing: 0.5px;
  }
  .wordmark__mark { width: 14px; height: 14px; background: var(--green); }
  .card--back .wordmark { left: 130px; top: 126px; font-size: 26px; }
  .card--front .wordmark { left: 34px; top: 118px; font-size: 20px; }
  .wordmark--small .wordmark__mark { width: 11px; height: 11px; }
  .holder {
    position: absolute; right: 110px; top: 58px; text-align: right;
  }
  .holder__name { font-size: 30px; font-weight: 700; color: var(--ink); line-height: 1.1; }
  .holder__title { font-size: 15px; font-weight: 400; color: var(--green); margin-top: 2px; }
  .contacts {
    position: absolute; left: 34px; bottom: 34px; list-style: none;
  }
  .contacts__item {
    display: flex; align-items: center; gap: 8px;
    font-size: 11px; color: var(--ink); line-height: 20px;
  }
  .contacts__icon { width: 13px; height: 13px; flex: none; }
</style>
</head>
<body>
<main class="sheet">

  <section class="card card--back" aria-label="Card back">
    <div class="card__accent" role="img" aria-label="Decorative green and charcoal wave band"></div>
    <div class="wordmark"><span class="wordmark__mark"></span>Tarvel Ridge</div>
  </section>

  <section class="card card--front" aria-label="Card front">
    <div class="card__accent" role="img" aria-label="Decorative green and charcoal wave band"></div>

    <div class="wordmark wordmark--small"><span class="wordmark__mark"></span>Tarvel Ridge</div>

    <div class="holder">
      <h1 class="holder__name">Pavel Orlinsky</h1>
      <p class="holder__title">Fund Manager</p>
    </div>

    <ul class="contacts">
      <li class="contacts__item">
        <svg class="contacts__icon" viewBox="0 0 14 14" aria-hidden="true">
          <circle cx="7" cy="7" r="6.2" fill="none" stroke="var(--green)" stroke-width="1.2"/>
          <rect x="4" y="5" width="6" height="4.2" fill="none" stroke="var(--green)" stroke-width="0.9"/>
          <path d="M4,5 L7,7.3 L10,5" fill="none" stroke="var(--green)" stroke-width="0.9"/>
        </svg>
        po@FundTarvel.example
      </li>
      <li class="contacts__item">
        <svg class="contacts__icon" viewBox="0 0 14 14" aria-hidden="true">
          <circle cx="7" cy="7" r="6.2" fill="none" stroke="var(--green)" stroke-width="1.2"/>
          <circle cx="7" cy="7" r="3" fill="none" stroke="var(--green)" stroke-width="0.9"/>
          <path d="M4,7 H10 M7,4 C5.8,5.5 5.8,8.5 7,10 M7,4 C8.2,5.5 8.2,8.5 7,10" fill="none" stroke="var(--green)" stroke-width="0.7"/>
        </svg>
        www.FundTarvel.example
      </li>
      <li class="contacts__item">
        <svg class="contacts__icon" viewBox="0 0 14 14" aria-hidden="true">
          <circle cx="7" cy="7" r="6.2" fill="none" stroke="var(--green)" stroke-width="1.2"/>
          <path d="M4.6,4.2 L5.8,4 L6.4,5.6 L5.7,6.2 C6.1,7.1 6.9,7.9 7.8,8.3 L8.4,7.6 L10,8.2 L9.8,9.4 C7,9.6 4.4,7 4.6,4.2 Z" fill="var(--green)"/>
        </svg>
        +1 555 284 6193
      </li>
    </ul>
  </section>

</main>
</body>
</html>
```